Brochure for a shopping mall

looking for brochure design to market a shopping center for tenants to lease space from us landlords.

THE IDEA IS TO PROMOTE THIS shopping MALL AS a LUXURY ELEGANT SPACE FOR TENANTS. Spaces are available for retail stores as well as Offices and medical and dental offices

PLAN IS TO PRINT ON PRESSLEAF.COM 25.5" x 11" TEMPLATE. I uploaded a basic plan. But i want you to do

GREY HARROW MALL
2738 GREY HARROW BLVD
ALPHARETTA GA 30005

FOR LEASE 404 617 2284

PLEASE DOWNLOAD PHOTOS FROM THIS LINK
http://www.quorela.com/2014/04/Building-Photos-3/n-8K4rw/
Updates

Guys,

This is a committed project. 
Kindly send in your designs. We are looking for a luxury look to showcase this mall as a high end place

The small design I posted can be changed anyway. Use your imagination to make all the changes. 
The design should be able to be printed on 25.5" X 11 format on pressleaf.com.

I also need to include SOME MINOR details  like a small mapzio map and number of parking spaces 262 traffic count.

some description of building like
Italian Florence Dome design with French architecture influence, newly built in 2007.
Imported Limestone walls and flooring and Mediterranean tiles.
Ideally suited for Retail store or office space including medical and dental offices.
A Class "A" building in Class "A" location

I am looking for front and back designs for the 25.5 inches X 11 inches TRIFOLD brochures.

Reason: No more extensions after this deadline. I really need something with a Luxury Look. on a trifold pattern. Only One goal of the Brochure is to attract New Tenants to rent space fro this shopping center

Reason: No more designs are being accepted. We will invite 2 designers to provide final designs and finalize one. Thank You for wonderful job

Reason: No new designs are being accepted. This is to finalize existing designs only

```html
<!DOCTYPE html>
<html lang="en">
<head>
<meta charset="utf-8">
<title>Grey Harrow Mall – Leasing Brochure</title>
<link href="https://fonts.googleapis.com/css2?family=Marcellus&family=Questrial&display=swap" rel="stylesheet">
<style>
  :root {
    --backdrop: #e8e7e3;
    --panel-dark: #2c2c2c;
    --panel-dark-edge: #232323;
    --band: #1c1c1c;
    --gold: #d6a94c;
    --gold-soft: #c99b45;
    --text-light: #e6e1d6;
    --title-dark: #2b2b2b;
    --cover-sky-top: #f6f6f6;
    --cover-sky-bottom: #e6e8ea;
  }
  * { box-sizing: border-box; margin: 0; padding: 0; }
  html, body { width: 1200px; height: 803px; overflow: hidden; }
  body {
    background: var(--backdrop);
    font-family: "Questrial", "Century Gothic", sans-serif;
    position: relative;
  }
  h1, h2 { font-weight: 400; }
  .brochure {
    position: absolute;
    left: 36px; top: 105px;
    width: 1128px; height: 540px;
    display: flex;
    box-shadow: 0 6px 18px rgba(0,0,0,.18);
  }
  .panel {
    position: relative;
    width: 376px; height: 100%;
    background: linear-gradient(180deg, var(--panel-dark) 0%, var(--panel-dark-edge) 100%);
    overflow: hidden;
  }
  .band {
    position: absolute;
    left: 0; right: 0; bottom: 0;
    height: 87px;
    background: var(--band);
    border-top: 2px solid var(--gold);
  }

  /* Panel 1 – spaces */
  .interior-photo {
    position: absolute; left: 14px; top: 10px; width: 366px; height: 266px;
    background: linear-gradient(165deg,
      #d8962e 0%, #e9b45a 12%, #f3e6cf 26%, #fbfbfa 40%,
      #e4ddd2 52%, #b98a55 64%, #8e5a2c 80%, #5e3818 100%);
  }
  .spaces-heading {
    position: absolute; left: 30px; top: 302px;
    color: var(--gold); font-size: 15px; letter-spacing: .5px;
  }
  .gold-rule { position: absolute; height: 1px; background: var(--gold-soft); }
  .features {
    position: absolute; left: 38px; top: 346px; width: 320px;
    list-style: disc; color: var(--gold);
  }
  .features li { font-size: 9.5px; line-height: 1.3; margin-bottom: 12px; padding-left: 2px; }
  .available {
    position: absolute; left: 0; right: 0; top: 28px;
    text-align: center; color: var(--gold);
  }
  .available .label { font-size: 15px; letter-spacing: .6px; }
  .available .size { font-size: 15px; font-weight: bold; letter-spacing: .4px; }

  /* Panel 2 – contact */
  .mall-name-small {
    position: absolute; left: 0; right: 0; top: 132px; text-align: center;
    font-family: "Marcellus", serif; color: var(--gold); font-size: 15px; letter-spacing: .6px;
  }
  .area-map {
    position: absolute; left: 100px; top: 170px; width: 178px; height: 100px;
    border: 2px solid var(--gold-soft);
    background: linear-gradient(155deg, #ececea 0%, #e2e2df 45%, #d6d6d3 100%);
  }
  .contact {
    position: absolute; left: 0; right: 0; top: 291px; text-align: center;
    color: var(--gold); font-size: 8.5px; line-height: 1.45; font-style: normal;
  }
  .leasing { position: absolute; left: 0; right: 0; top: 347px; text-align: center; color: var(--gold); }
  .leasing .label { font-size: 8.5px; letter-spacing: .3px; }
  .leasing .phone { font-size: 12px; font-weight: bold; letter-spacing: .5px; margin-top: 2px; }
  .disclaimer {
    position: absolute; left: 10px; right: 10px; top: 12px; text-align: center;
    color: var(--text-light); font-size: 5px; line-height: 1.35;
  }
  .disclaimer .title { font-weight: bold; font-size: 6px; margin-bottom: 1px; }
  .copyright {
    position: absolute; left: 0; right: 0; top: 58px; text-align: center;
    color: var(--text-light); font-size: 5px; line-height: 1.3;
  }

  /* Panel 3 – cover */
  .panel.cover {
    background: linear-gradient(180deg, var(--cover-sky-top) 0%, var(--cover-sky-bottom) 60%);
  }
  .cover-title {
    position: absolute; left: 0; right: 0; top: 90px; text-align: center;
    font-family: "Marcellus", serif; color: var(--title-dark); font-size: 27px; letter-spacing: 1px;
  }
  .cover-address {
    position: absolute; left: 0; right: 0; top: 128px; text-align: center;
    color: var(--gold); font-size: 10.5px; letter-spacing: .5px;
  }
  .building-photo {
    position: absolute; left: 0; right: 0; top: 215px; height 238px; height: 238px;
    background: linear-gradient(180deg,
      rgba(230,232,234,0) 0%, #dfe0e0 18%, #d3d0ca 38%, #e9e6e0 50%,
      #b7aa96 64%, #7a6a58 78%, #4f4842 88%, #a7a29b 100%);
  }
  .tagline {
    position: absolute; left: 0; right: 0; top: 34px; text-align: center;
    color: var(--gold); font-size: 12px; font-style: italic;
  }
</style>
</head>
<body>
  <main class="brochure">
    <section class="panel panel-spaces">
      <div class="interior-photo" role="img" aria-label="Photo of a bright empty retail interior with orange walls, polished floor and glass storefront"></div>
      <h2 class="spaces-heading">RETAIL OFFICE/ MEDICAL - DENTAL</h2>
      <div class="gold-rule" style="left:30px; right:18px; top:324px;"></div>
      <ul class="features">
        <li>Italian Florence Dome design with French architecture influence, newly built in 2007.</li>
        <li>Imported Limestone walls and flooring and Mediterranean tiles.</li>
        <li>Ideally suited for Retail store or office space including medical and dental offices.</li>
      </ul>
      <div class="band">
        <div class="available">
          <div class="label">AVAILABLE SPACES FROM</div>
          <div class="size">1,176 TO 15,000 SQ.FT.</div>
        </div>
      </div>
    </section>

    <section class="panel panel-contact">
      <h2 class="mall-name-small">GREY HARROW MALL</h2>
      <div class="gold-rule" style="left:112px; right:112px; top:158px;"></div>
      <div class="area-map" role="img" aria-label="Small street map showing the mall location"></div>
      <address class="contact">
        GREY HARROW MALL<br>
        2738 Grey Harrow Blvd<br>
        Alpharetta, GA 30005
      </address>
      <div class="leasing">
        <div class="label">NOW LEASING</div>
        <div class="phone">404 617 2284</div>
      </div>
      <div class="band">
        <div class="disclaimer">
          <div class="title">Disclaimer:</div>
          All details in this brochure are given for general guidance only and do not form part of any lease offer or contract. Floor areas, layouts and suite availability may change without notice. Prospective tenants should verify all measurements, terms and permitted uses directly with the leasing office before making any commitment.
        </div>
        <div class="copyright">© 2014 Grey Harrow Mall<br>All rights reserved.</div>
      </div>
    </section>

    <section class="panel cover">
      <h1 class="cover-title">GREY HARROW MALL</h1>
      <p class="cover-address">2738 GREY HARROW BLVD, ALPHARETTA GA 30005</p>
      <div class="building-photo" role="img" aria-label="Photo of the mall exterior with a limestone tower and lit storefronts at dusk"></div>
      <div class="band">
        <p class="tagline">Welcome to Elegance and Luxury</p>
      </div>
    </section>
  </main>
</body>
</html>
```